Mirelo Japanese Restaurant

We just want the japanese sakura background and the menu as below

Side dish :
Edamame $4
Japanese Steam Green Bean
Crab Craw $3 each
With Japanese mayo
Teriyaki Chicken stick $3 each
Chicken stick with home made teriyaki sauce
Tempura Prawns $7
With Japanese mayo
Miso Soup $3
Traditional Japanese soup
Salt and Pepper Calamari $7
With japanese mayo

Main dish:
Gyu Don $12
Bowl of steam rice topped with beef and onion simmered in a mildly sweet sauce.
Teriyaki Don $12
Bowl of steam rice topped with your choice of beef, chicken or pork and with our special Teriyaki sauce.
Vege Don $12
Bowl of steam rice with seasonal Vegetables with the special japanese sweet soy sauce.
Japanese Curry $12,(prawns $14)
Bowl of steam rice with Chicken, pork or prawn with japanese mild curry sauce.
Katsu Don $12
Bowl of steam rice topped with a deep-fried pork cutlet and egg with the japanese special sauce.
Oyako Don $12
Bowl of steam rice topped with chick and egg with japanese special sauce.
Spice Don $12
Bowl of steam rice topped with beef or chicken with japanese spice sauce.
Gingle Don $12
Bowl of steam rice topped with beef or chicken with japanese ginger sauce.
Sushi $3
Roll everyday on seasonal
ingredient.

Japanese-style sweets
Black Sesame Ice cream $4.5
Green tea Ice cream $4.5

```html
<!DOCTYPE html>
<html lang="en">
<head>
<meta charset="utf-8">
<title>Mirelo Japanese Restaurant – Menu</title>
<link rel="stylesheet" href="https://fonts.googleapis.com/css2?family=Arimo:wght@400;700&family=Libre+Baskerville:wght@400;700&family=Cormorant+SC:wght@500&display=swap">
<style>
  :root {
    --backdrop: #e6e3de;
    --paper: #f4f4f2;
    --sky: #c3e3f3;
    --rule: #3d4a55;
    --ink: #2b211c;
    --item: #5b2f1c;
    --muted: #6e6a66;
    --food-warm: #d9782f;
    --food-deep: #b5531d;
    --leaf: #9cc95a;
  }
  * { margin: 0; padding: 0; box-sizing: border-box; }
  html, body { width: 1200px; height: 856px; overflow: hidden; }
  body { background: var(--backdrop); position: relative; font-family: "Arimo", Arial, sans-serif; color: var(--ink); }

  .page { position: absolute; top: 65px; width: 536px; height: 757px; background: var(--paper); box-shadow: 0 2px 8px rgba(0,0,0,.25); overflow: hidden; }
  .page--front { left: 42px; }
  .page--back { left: 620px; }

  .front-art { position: absolute; inset: 0; }

  .brand { position: absolute; font-family: "Libre Baskerville", Georgia, serif; font-weight: 700; color: var(--ink); }
  .brand__mark { position: absolute; border-radius: 50%; background: #f2c9d0; border: 1px solid #8a7a7a; }
  .brand--cover .brand__mark { left: 194px; top: 260px; width: 70px; height: 70px; }
  .brand--cover .brand__name { position: absolute; left: 328px; top: 256px; font-size: 26px; letter-spacing: 3px; white-space: nowrap; }
  .brand--cover .brand__tag { position: absolute; left: 278px; top: 305px; font-size: 18px; white-space: nowrap; }

  .photo { position: absolute; }

  .section-title { position: absolute; font-family: "Libre Baskerville", Georgia, serif; font-weight: 400; font-size: 19px; letter-spacing: .5px; text-transform: uppercase; border-bottom: 1.5px solid var(--ink); padding-bottom: 1px; line-height: 1.1; white-space: nowrap; }
  .section-title--side { left: 13px; top: 17px; }
  .section-title--main { left: 207px; top: 312px; }
  .section-title--sweets { left: 123px; top: 570px; }

  .menu-list { position: absolute; list-style: none; }
  .menu-item { position: relative; padding-left: 8px; }
  .menu-item::before { content: "•"; position: absolute; left: 0; top: 0; font-size: 10px; color: var(--item); }
  .menu-item__name { font-weight: 700; font-size: 10.5px; color: var(--item); }
  .menu-item__price { font-size: 12.5px; color: var(--item); }
  .menu-item__unit { font-size: 9px; color: var(--item); }
  .menu-item__desc { display: block; font-size: 8px; line-height: 11px; color: var(--muted); }

  .menu-list--side { left: 14px; top: 53px; width: 230px; }
  .menu-list--side .menu-item { height: 34px; }
  .menu-list--main { top: 351px; width: 190px; }
  .menu-list--main-left { left: 68px; }
  .menu-list--main-right { left: 270px; }
  .menu-list--main .menu-item { height: 50px; }
  .menu-list--main .menu-item__price { font-size: 11.5px; }
  .menu-list--sweets { left: 195px; top: 604px; }
  .menu-list--sweets .menu-item { height: 24px; }
  .menu-list--sweets .menu-item__name { font-size: 9.5px; }

  .footer-brand .brand__mark { left: 14px; top: 702px; width: 38px; height: 38px; }
  .footer-brand .brand__name { position: absolute; left: 96px; top: 699px; font-size: 14px; letter-spacing: 2px; white-space: nowrap; }
  .footer-brand .brand__tag { position: absolute; left: 76px; top: 718px; font-size: 11px; white-space: nowrap; }
  .footer-divider { position: absolute; left: 218px; top: 699px; width: 1px; height: 40px; background: var(--ink); }
  .contact { position: absolute; left: 232px; top: 702px; font-family: "Cormorant SC", Georgia, serif; font-weight: 500; font-size: 15px; line-height: 16px; letter-spacing: .6px; color: var(--ink); }
</style>
</head>
<body>

<section class="page page--front" aria-label="Menu cover">
  <svg class="front-art" width="536" height="757" viewBox="0 0 536 757">
    <defs>
      <radialGradient id="cover-food" cx="45%" cy="45%" r="70%">
        <stop offset="0" stop-color="var(--food-warm)"/>
        <stop offset=".55" stop-color="var(--food-deep)"/>
        <stop offset="1" stop-color="var(--leaf)"/>
      </radialGradient>
    </defs>
    <polygon points="186,0 536,0 536,757 158,757" fill="var(--sky)"/>
    <line x1="186" y1="0" x2="158" y2="757" stroke="var(--rule)" stroke-width="2"/>
    <path class="photo" role="img" aria-label="Photo of crispy fried chicken pieces on lettuce"
          d="M228,757 L228,380 C250,360 300,355 340,370 C400,392 450,395 490,375 C512,364 528,360 536,362 L536,757 Z"
          fill="url(#cover-food)"/>
  </svg>
  <div class="brand brand--cover">
    <span class="brand__mark"></span>
    <span class="brand__name">MIRELO</span>
    <span class="brand__tag">Japanese Restaurant</span>
  </div>
</section>

<section class="page page--back" aria-label="Menu">
  <svg class="photo" style="left:0;top:0" width="536" height="757" viewBox="0 0 536 757">
    <defs>
      <radialGradient id="back-food" cx="60%" cy="55%" r="70%">
        <stop offset="0" stop-color="var(--food-warm)"/>
        <stop offset=".6" stop-color="var(--food-deep)"/>
        <stop offset="1" stop-color="var(--leaf)"/>
      </radialGradient>
    </defs>
    <path role="img" aria-label="Photo of crispy fried chicken pieces on lettuce"
          d="M295,0 L536,0 L536,272 C505,268 470,268 430,262 C380,256 330,272 300,250 C275,230 280,190 290,160 C300,130 282,100 280,70 C278,40 285,15 295,0 Z"
          fill="url(#back-food)"/>
  </svg>

  <h2 class="section-title section-title--side">Side Dish</h2>
  <ul class="menu-list menu-list--side">
    <li class="menu-item"><span class="menu-item__name">Edamame</span> <span class="menu-item__price">$4</span><span class="menu-item__desc">Japanese Steam Green Bean</span></li>
    <li class="menu-item"><span class="menu-item__name">Crab Craw</span> <span class="menu-item__price">$3</span> <span class="menu-item__unit">each</span><span class="menu-item__desc">With Japanese mayo</span></li>
    <li class="menu-item"><span class="menu-item__name">Teriyaki Chicken stick</span> <span class="menu-item__price">$3 each</span><span class="menu-item__desc">Chicken stick with home made teriyaki sauce</span></li>
    <li class="menu-item"><span class="menu-item__name">Tempura Prawns</span> <span class="menu-item__price">$7</span><span class="menu-item__desc">With Japanese mayo</span></li>
    <li class="menu-item"><span class="menu-item__name">Miso Soup</span> <span class="menu-item__price">$3</span><span class="menu-item__desc">Traditional Japanese soup</span></li>
    <li class="menu-item"><span class="menu-item__name">Salt and Pepper Calamari</span> <span class="menu-item__price">$7</span><span class="menu-item__desc">With japanese mayo</span></li>
  </ul>

  <h2 class="section-title section-title--main">Main Dish</h2>
  <ul class="menu-list menu-list--main menu-list--main-left">
    <li class="menu-item"><span class="menu-item__name">Gyu Don</span> <span class="menu-item__price">$12</span><span class="menu-item__desc">Bowl of steam rice topped with beef and onion simmered in a mildly sweet sauce.</span></li>
    <li class="menu-item"><span class="menu-item__name">Teriyaki Don</span> <span class="menu-item__price">$12</span><span class="menu-item__desc">Bowl of steam rice topped with your choice of beef, chicken or pork and with our special Teriyaki sauce.</span></li>
    <li class="menu-item"><span class="menu-item__name">Vege Don</span> <span class="menu-item__price">$12</span><span class="menu-item__desc">Bowl of steam rice with seasonal Vegetables with the special japanese sweet soy sauce.</span></li>
    <li class="menu-item"><span class="menu-item__name">Japanese Curry</span> <span class="menu-item__price">$12</span><span class="menu-item__unit">,(prawns $14)</span><span class="menu-item__desc">Bowl of steam rice with Chicken, pork or prawn with japanese mild curry sauce.</span></li>
  </ul>
  <ul class="menu-list menu-list--main menu-list--main-right">
    <li class="menu-item"><span class="menu-item__name">Oyako Don</span> <span class="menu-item__price">$12</span><span class="menu-item__desc">Bowl of steam rice topped with chick and egg with japanese special sauce.</span></li>
    <li class="menu-item"><span class="menu-item__name">Spice Don</span> <span class="menu-item__price">$12</span><span class="menu-item__desc">Bowl of steam rice topped with beef or chicken with japanese spice sauce.</span></li>
    <li class="menu-item"><span class="menu-item__name">Gingle Don</span> <span class="menu-item__price">$12</span><span class="menu-item__desc">Bowl of steam rice topped with beef or chicken with japanese ginger sauce.</span></li>
    <li class="menu-item"><span class="menu-item__name">Sushi</span> <span class="menu-item__price">$3</span><span class="menu-item__desc">Roll everyday on seasonal ingredient.</span></li>
  </ul>

  <h2 class="section-title section-title--sweets">Japanese-Style Sweets</h2>
  <ul class="menu-list menu-list--sweets">
    <li class="menu-item"><span class="menu-item__name">Black Sesame Ice cream</span> <span class="menu-item__price">$4.5</span></li>
    <li class="menu-item"><span class="menu-item__name">Green tea Ice cream</span> <span class="menu-item__price">$4.5</span></li>
  </ul>

  <div class="brand footer-brand">
    <span class="brand__mark"></span>
    <span class="brand__name">MIRELO</span>
    <span class="brand__tag">Japanese Restaurant</span>
  </div>
  <span class="footer-divider"></span>
  <p class="contact">Put Your Address<br>Contact Information here</p>
</section>

</body>
</html>
```